I need a book cover for my book titled Sunny Porch! The subtitle is Quiet Orchard Days and the the author is Marisol Dunleavy. I want the attached photo included on the cover, plus the words "I never met a chicken wing I didn't like!" The book size is 5.06 x 7.81 in. and is 146 pages. For the color scheme, I like a chocolate brown cover with aqua blue letters. (Please note that you don't have to use these colors. Feel free to use this color scheme or whatever you colors you like!)

• Please include my photo for the back cover, along with this text:

Sunny Porch! I was tired of being tired! I was tired of acid reflux, body stiffness, and being overweight. To make matters worse, I suffered from back pain, constipation, leg pain, and lack of sleep. If you are tired of looking to medical test for your answers, this is the book for you. The key was the day I decided to make “me” a priority by being #1 on my “to-do” list.

Our healthcare system seems to be more concerned about treating illness than they are about preventing it; which is why we have so many problems with our health and wellness. That’s why I’m going to give you insights into nutrition, health care, and the pharmaceutical industry.

I’m also going to give you some insights into exercise, supplements, detoxing and essential oils; as well as what goes into your grocery cart and the foods you feed your family.

Because you’re reading this I know you’re ready to live your best life, Sunny Porch! is for you.

Here’s to a healthy you!

Here's a brief bio about the author for the back cover:

Marisol lives in Chicago with her husband, Dr. Wendell, and has three adult children. She is probably one of the most private people you will meet – BUT HAD to tell her story!

```html
<!DOCTYPE html>
<html lang="en">
<head>
<meta charset="utf-8">
<title>Sunny Porch! — Cover Spread</title>
<link href="https://fonts.googleapis.com/css2?family=Cinzel:wght@400;700&family=Kaushan+Script&display=swap" rel="stylesheet">
<style>
  :root {
    --page-bg: #efefef;
    --brown-deep: #4a2419;
    --brown-mid: #623226;
    --brown-warm: #7d4735;
    --brown-glow: #8e5a45;
    --band-light: #8c5b40;
    --band-dark: #4b2218;
    --ink-cream: #fbf6ef;
    --ink-soft: #efe3d6;
    --photo-sauce: #a8442a;
    --photo-dish: #f4f1ec;
    --photo-celery: #b9d48a;
  }
  * { box-sizing: border-box; margin: 0; padding: 0; }
  html, body { width: 1200px; height: 800px; overflow: hidden; }
  body {
    background: var(--page-bg);
    font-family: "Cinzel", Georgia, serif;
    color: var(--ink-cream);
    position: relative;
  }
  .spread {
    position: absolute;
    left: 131px; top: 50px;
    width: 938px; height: 700px;
    display: flex;
    box-shadow: 0 14px 30px rgba(0,0,0,.25);
  }
  .cover {
    position: relative;
    width: 454px; height: 700px;
    overflow: hidden;
    background:
      radial-gradient(ellipse 70% 40% at 40% 45%, rgba(160,100,75,.45), transparent 70%),
      linear-gradient(170deg, var(--brown-warm) 0%, var(--brown-mid) 45%, var(--brown-warm) 75%, var(--brown-deep) 100%);
  }
  .spine {
    width: 30px; height: 700px;
    background: linear-gradient(90deg, var(--brown-deep), var(--brown-mid) 50%, var(--brown-deep));
  }
  .title {
    font-weight: 700;
    text-align: center;
    line-height: 1;
    text-shadow: 0 2px 4px rgba(0,0,0,.45);
  }
  .subtitle {
    text-align: center;
    font-weight: 400;
    text-shadow: 0 2px 3px rgba(0,0,0,.4);
  }

  /* back cover */
  .back .title { margin-top: 44px; font-size: 42px; }
  .back .subtitle { font-size: 22px; margin-top: 4px; }
  .blurb {
    margin: 26px 38px 0;
    font-size: 9.6px;
    line-height: 1.42;
    color: var(--ink-soft);
  }
  .blurb p { margin-bottom: 9px; }
  .dots {
    display: flex; justify-content: flex-end; gap: 4px;
    margin: 2px 38px 0;
  }
  .dots span { width: 7px; height: 7px; border-radius: 50%; background: var(--ink-soft); }
  .bio {
    margin: 14px 38px 0;
    font-size: 11.5px;
    line-height: 1.45;
    color: var(--ink-soft);
  }
  .bio p { margin-bottom: 10px; }
  .byline {
    position: absolute; left: 38px; bottom: 48px;
    font-size: 11px;
  }
  .byline .label {
    display: block;
    padding-bottom: 3px;
    border-bottom: 1px solid var(--ink-soft);
    width: 150px;
  }
  .byline .name { display: block; font-size: 16px; margin-top: 6px; }

  /* front cover */
  .front .title { margin-top: 64px; font-size: 56px; }
  .front .subtitle { font-size: 29px; margin-top: 10px; }
  .food-photo {
    position: absolute;
    left: 40px; top: 232px;
    width: 374px; height: 250px;
    border-radius: 18px;
    background:
      radial-gradient(ellipse 30% 30% at 36% 25%, var(--photo-celery), transparent 70%),
      radial-gradient(ellipse 32% 28% at 62% 60%, var(--photo-sauce), transparent 75%),
      radial-gradient(ellipse 60% 42% at 50% 60%, var(--photo-dish), transparent 80%);
  }
  .quote {
    position: absolute;
    left: 20px; top: 500px; width: 414px;
    font-family: "Kaushan Script", cursive;
    font-size: 27px;
    line-height: 1.25;
    text-align: center;
    transform: rotate(7deg);
    text-shadow: 0 2px 3px rgba(0,0,0,.5);
    z-index: 2;
  }
  .author-band {
    position: absolute; left: 0; right: 0; bottom: 34px;
    height: 90px;
    background: var(--band-dark);
  }
  .author-band::before {
    content: ""; position: absolute; left: 0; right: 0; top: 0; height: 34px;
    background: var(--band-light);
  }
  .author-band::after {
    content: ""; position: absolute; left: 0; right: 0; bottom: -34px; height: 34px;
    background: var(--band-light);
  }
  .author-name {
    position: absolute; left: 0; right: 0; top: 38px;
    text-align: center;
    font-size: 21px;
    letter-spacing: .5px;
    text-shadow: 0 2px 3px rgba(0,0,0,.5);
  }
</style>
</head>
<body>
  <main class="spread">
    <section class="cover back">
      <h2 class="title">Sunny Porch!</h2>
      <p class="subtitle">Quiet Orchard Days</p>
      <div class="blurb">
        <p>Sunny Porch! I was tired of being tired! I was tired of acid reflux, body stiffness, and being overweight. To make matters worse, I suffered from back pain, constipation, leg pain, and lack of sleep. If you are tired of looking to medical test for your answers, this is the book for you. The key was the day I decided to make “me” a priority by being #1 on my “to-do” list.</p>
        <p>Our healthcare system seems to be more concerned about treating illness than they are about preventing it; which is why we have so many problems with our health and wellness. That’s why I’m going to give you insights into nutrition, health care, and the pharmaceutical industry.</p>
        <p>I’m also going to give you some insights into exercise, supplements, detoxing and essential oils; as well as what goes into your grocery cart and the foods you feed your family.</p>
        <p>Because you’re reading this I know you’re ready to live your best life, Sunny Porch! is for you.</p>
      </div>
      <div class="dots" aria-hidden="true"><span></span><span></span><span></span></div>
      <div class="bio">
        <p>Marisol lives in Chicago with her husband, Dr. Wendell, and has three adult children.</p>
        <p>She is probably one of the most private people you will meet – but had to tell her story!</p>
      </div>
      <p class="byline"><span class="label">Author</span><span class="name">Marisol Dunleavy</span></p>
    </section>

    <div class="spine" aria-hidden="true"></div>

    <section class="cover front">
      <h1 class="title">Sunny Porch!</h1>
      <p class="subtitle">Quiet Orchard Days</p>
      <div class="food-photo" role="img" aria-label="Photo of saucy chicken wings in a white dish with a ramekin of ranch dip, celery and carrot sticks"></div>
      <p class="quote">“I never met a chicken wing<br>I didn’t like!”</p>
      <div class="author-band">
        <p class="author-name">Marisol Dunleavy</p>
      </div>
    </section>
  </main>
</body>
</html>
```